Concierge Healthcare Business Card Design and Logo

We need a logo and business card design for a new company called "Sound Keeper". We will provide concierge audiological care, hearing aids, hearing exams, custom hearing protection etc to patients in the comfort of their homes and offices. We would like a sleek and modern design preferably with an Ear related logo.

Target Market(s)

People with hearing loss, Hunters, Musicians
My usual clientele are older individuals so usually 50+ years old

Industry/Entity Type

Health Care

Contact Information for Business Card

Clara Whitfield, AuD
Audiologist
512-418-2967
soundkeeper@mailvista.net
www.soundkeeperclinic.net

Logo Text

Sound Keeper

Number of Pages Required

3 page

```html
<!DOCTYPE html>
<html lang="en">
<head>
<meta charset="utf-8">
<title>Sound Keeper – Business Card</title>
<link rel="stylesheet" href="https://fonts.googleapis.com/css2?family=Open+Sans:ital,wght@0,400;0,700;1,700&display=swap">
<style>
  :root {
    --page: #ffffff;
    --slate: #6b7a85;
    --orange: #f0832f;
    --green: #9dc93b;
    --brace: #e6e8ea;
  }
  html, body {
    margin: 0;
    padding: 0;
    width: 1200px;
    height: 732px;
    overflow: hidden;
    background: var(--page);
    font-family: "Open Sans", Arial, sans-serif;
  }
  .card {
    position: absolute;
    left: 48px;
    top: 48px;
    width: 1108px;
    height: 634px;
    background: var(--slate);
  }
  .brand {
    position: absolute;
    left: 78px;
    top: 222px;
    display: flex;
    align-items: center;
    gap: 22px;
  }
  .brand-dot {
    width: 70px;
    height: 70px;
    border-radius: 50%;
    background: var(--green);
    flex: none;
  }
  .brand-name {
    margin: 0;
    color: var(--orange);
    font-weight: 700;
    font-size: 60px;
    line-height: 1.05;
    letter-spacing: 2px;
    text-transform: uppercase;
  }
  .brace {
    position: absolute;
    left: 0;
    top: 0;
    width: 1108px;
    height: 634px;
  }
  .contact {
    position: absolute;
    left: 622px;
    top: 0;
    margin: 0;
    padding: 0;
    list-style: none;
    font-weight: 700;
  }
  .contact li {
    position: absolute;
    left: 0;
    white-space: nowrap;
  }
  .contact-name  { top: 110px; font-size: 32px; color: var(--orange); }
  .contact-role  { top: 202px; font-size: 30px; color: var(--orange); text-decoration: underline; text-underline-offset: 5px; text-decoration-thickness: 2px; }
  .contact-phone { top: 294px; font-size: 31px; color: var(--green); font-style: italic; }
  .contact-email { top: 390px; font-size: 28px; color: var(--green); }
  .contact-web   { top: 474px; font-size: 28px; color: var(--green); }
</style>
</head>
<body>
  <section class="card">
    <div class="brand">
      <span class="brand-dot"></span>
      <h1 class="brand-name">Sound<br>Keeper</h1>
    </div>

    <svg class="brace" viewBox="0 0 1108 634" aria-hidden="true">
      <path d="M622 58 C575 60 552 90 552 150 L552 255 C552 295 530 312 484 317 C530 322 552 339 552 379 L552 484 C552 544 575 574 622 576"
            fill="none" stroke="var(--brace)" stroke-width="20" stroke-linecap="butt"/>
    </svg>

    <ul class="contact">
      <li class="contact-name">Clara Whitfield, AuD</li>
      <li class="contact-role">AUDIOLOGIST</li>
      <li class="contact-phone">512-418-2967</li>
      <li class="contact-email">soundkeeper@mailvista.net</li>
      <li class="contact-web">www.soundkeeperclinic.net</li>
    </ul>
  </section>
</body>
</html>
```